Biz Card Physical Therapy Company
Lorimer Physical Therapy
Bright & Fun-filled
Darnell Okoro, PT, CIMT, CSCS
Director
4172 W Fenwick Ave,
Marlow Heights, CA 90612
LorimerTherapy@quillpost.com
CA PT 61803
Please feel free to move the logo to the side of the tag-line, or however you may see fit
vector logo file

```html
<!DOCTYPE html>
<html lang="en">
<head>
<meta charset="UTF-8">
<title>Lorimer Physical Therapy – Business Card</title>
<link href="https://fonts.googleapis.com/css2?family=Roboto+Slab:wght@700;800&family=Source+Sans+3:ital,wght@0,400;0,600;1,400&display=swap" rel="stylesheet">
<style>
  :root {
    --bg: #e9ecea;
    --card: #ffffff;
    --green: #3f8a2e;
    --green-dark: #2c6a1f;
    --green-light: #6fb043;
    --ink: #2f3330;
    --grey: #6b6f6c;
    --swoosh: #4a4d4b;
    --faint: #e2e5e3;
  }
  * { margin: 0; padding: 0; box-sizing: border-box; }
  html, body { width: 1200px; height: 974px; overflow: hidden; }
  body { background: var(--bg); font-family: "Source Sans 3", sans-serif; position: relative; }

  .card {
    position: absolute;
    width: 700px; height: 400px;
    background: var(--card);
    border-radius: 22px;
    overflow: hidden;
    box-shadow: 0 10px 28px rgba(0,0,0,.14);
  }
  .card--back { left: 440px; top: 70px; background: linear-gradient(135deg, #ffffff 0%, #f2f4f3 100%); }
  .card--front { left: 60px; top: 500px; }

  /* back */
  .back__web {
    position: absolute; left: 48px; top: 170px;
    font-size: 22px; letter-spacing: 3px; color: var(--grey);
  }
  .back__mark {
    position: absolute; right: 40px; bottom: 50px;
    display: flex; align-items: center; gap: 18px;
    font-family: "Roboto Slab", serif; font-weight: 800;
    font-size: 78px; color: var(--faint);
  }
  .back__mark .dot { width: 60px; height: 60px; border-radius: 50%; background: var(--faint); }

  /* front */
  .front__wave { position: absolute; inset: 0; width: 700px; height: 400px; }
  .brand { position: absolute; left: 42px; top: 30px; }
  .brand__mark {
    display: flex; align-items: center; gap: 10px;
    font-family: "Roboto Slab", serif; font-weight: 800; font-size: 22px; color: var(--green);
  }
  .brand__mark .dot { width: 18px; height: 18px; border-radius: 50%; background: var(--green); }
  .brand__name {
    margin-top: 6px;
    font-family: "Roboto Slab", serif; font-weight: 800; font-size: 46px;
    letter-spacing: 2px; color: var(--green); line-height: 1;
  }
  .brand__sub {
    font-family: "Roboto Slab", serif; font-weight: 700; font-size: 22px;
    letter-spacing: 2px; color: var(--ink); margin-top: 4px;
  }
  .brand__tag {
    font-style: italic; font-size: 15px; color: var(--green); margin-top: 2px; letter-spacing: .5px;
  }
  .person { position: absolute; left: 44px; top: 212px; color: var(--grey); }
  .person__name { font-size: 15px; font-weight: 600; letter-spacing: 2px; }
  .person__role { font-size: 14px; letter-spacing: 2px; margin-top: 2px; }

  .contact {
    position: absolute; left: 380px; top: 252px;
    list-style: none; color: #fff; font-size: 13px; letter-spacing: .6px;
  }
  .contact li { display: flex; align-items: center; gap: 8px; line-height: 22px; white-space: nowrap; }
  .contact svg { width: 13px; height: 13px; flex: none; }
</style>
</head>
<body>

  <section class="card card--back" aria-label="Card back">
    <p class="back__web">www.LorimerPT.com</p>
    <div class="back__mark"><span class="dot"></span>LorimerPT</div>
  </section>

  <section class="card card--front" aria-label="Card front">
    <svg class="front__wave" viewBox="0 0 700 400" preserveAspectRatio="none" aria-hidden="true">
      <defs>
        <linearGradient id="band" x1="0" y1="0" x2="1" y2="1">
          <stop offset="0" stop-color="#6fb043"/>
          <stop offset=".55" stop-color="#3f8a2e"/>
          <stop offset="1" stop-color="#2c6a1f"/>
        </linearGradient>
      </defs>
      <path d="M0 300 C150 240 260 330 420 260 C540 205 620 140 700 110 L700 400 L0 400 Z" fill="url(#band)"/>
      <path d="M0 292 C150 230 260 318 420 248 C540 194 620 128 700 98 L700 108 C620 140 540 206 420 262 C260 332 150 244 0 304 Z" fill="#4a4d4b"/>
    </svg>

    <div class="brand">
      <div class="brand__mark"><span class="dot"></span>LorimerPT</div>
      <h1 class="brand__name">LORIMER</h1>
      <p class="brand__sub">PHYSICAL THERAPY</p>
      <p class="brand__tag">Recovery, Strength &amp; Movement</p>
    </div>

    <div class="person">
      <p class="person__name">Darnell Okoro, PT, CIMT, CSCS</p>
      <p class="person__role">Director</p>
    </div>

    <ul class="contact">
      <li><svg viewBox="0 0 12 12"><path d="M6 1a3.5 3.5 0 0 0-3.5 3.5C2.5 7 6 11 6 11s3.5-4 3.5-6.5A3.5 3.5 0 0 0 6 1zm0 4.8a1.3 1.3 0 1 1 0-2.6 1.3 1.3 0 0 1 0 2.6z" fill="#fff"/></svg>4172 W Fenwick Ave, Marlow Heights, CA 90612</li>
      <li><svg viewBox="0 0 12 12"><path d="M3 1l2 2.5-1.2 1.2a7 7 0 0 0 3.5 3.5L8.5 7 11 9l-1.5 2C5 10.5 1.5 7 1 2.5z" fill="#fff"/></svg>(562) 555-0148</li>
      <li><svg viewBox="0 0 12 12"><rect x="2" y="1" width="8" height="10" rx="1.5" fill="none" stroke="#fff" stroke-width="1.3"/><circle cx="6" cy="9" r=".8" fill="#fff"/></svg>(562) 555-0193</li>
      <li><svg viewBox="0 0 12 12"><rect x="1" y="2.5" width="10" height="7" rx="1" fill="none" stroke="#fff" stroke-width="1.2"/><path d="M1.5 3l4.5 3.5L10.5 3" fill="none" stroke="#fff" stroke-width="1.2"/></svg>LorimerTherapy@quillpost.com</li>
      <li><svg viewBox="0 0 12 12"><path d="M2 6.5l2.5 2.5L10 3" fill="none" stroke="#fff" stroke-width="1.6"/></svg>CA PT 61803</li>
    </ul>
  </section>

</body>
</html>
```